I am looking for a modern, clean and neat design for a reflexology and well being business. The business name is Lumen Orto (this is an old Latin word for wellbeing). The colours I would like are purple, white and grey. I am open to suggestions for pictures such as healing or working hands, a pair of feet, images that represent my business that you may think of....... or maybe you think no images at all would be best? My tag line is: "Relax, Renew, Revive" or "Find you balance......... Relax, Renew, Revive" I can decide which I want so I would like to see what both would look like. I would like space on the back to write the client's appointment date and time (more than once)

```html
<!DOCTYPE html>
<html lang="en">
<head>
<meta charset="utf-8">
<title>Lumen Orto Reflexology – Business Card</title>
<link rel="stylesheet" href="https://fonts.googleapis.com/css2?family=Open+Sans:wght@400;600;700&display=swap">
<style>
  :root {
    --purple: #5e2a8c;
    --purple-band: #6b3a9a;
    --grey-text: #6f6f6f;
    --grey-line: #8e8e8e;
    --grey-band: #9a9a9a;
    --card: #ffffff;
    --backdrop: #e8e6ea;
  }
  * { margin: 0; padding: 0; box-sizing: border-box; }
  html, body {
    width: 1200px; height: 1000px; overflow: hidden;
    background: var(--backdrop);
    font-family: "Open Sans", Arial, sans-serif;
  }
  .card {
    position: absolute; left: 265px; width: 666px; height: 397px;
    background: var(--card);
    box-shadow: 0 2px 8px rgba(0,0,0,.18);
    overflow: hidden;
  }
  .card--front { top: 73px; }
  .card--back { top: 533px; }

  .brand {
    position: absolute; display: flex; align-items: center; gap: 12px;
    color: var(--purple); font-weight: 400; font-size: 44px; line-height: 1;
    letter-spacing: -0.5px;
  }
  .brand__dot { width: 18px; height: 18px; border-radius: 50%; background: var(--purple); }
  .card--front .brand { right: 32px; top: 82px; }
  .card--back .brand { right: 50px; top: 76px; }

  .holder__accent { position: absolute; left: 0; top: 195px; width: 8px; height: 40px; background: var(--purple); }
  .holder__name { position: absolute; left: 33px; top: 191px; font-size: 22px; font-weight: 600; color: var(--purple); }
  .holder__role { position: absolute; left: 33px; top: 219px; font-size: 16px; color: var(--grey-text); }
  .divider { position: absolute; left: 33px; right: 32px; top: 252px; height: 2px; background: var(--grey-line); }

  .contacts { position: absolute; left: 33px; top: 267px; list-style: none; }
  .contacts li { display: flex; align-items: center; gap: 7px; height: 23.5px; font-size: 16px; color: var(--grey-text); }
  .contacts svg { width: 15px; height: 15px; fill: var(--purple); }

  .address { position: absolute; right: 32px; top: 289px; text-align: right; font-size: 16px; line-height: 24px; color: var(--grey-text); font-style: normal; }

  .band-grey { position: absolute; left: 0; bottom: 0; width: 345px; height: 18px; background: var(--grey-band); clip-path: polygon(0 0, 100% 0, 94% 100%, 0 100%); }
  .band-tagline {
    position: absolute; right: 0; bottom: 0; width: 336px; height: 33px;
    background: var(--purple-band);
    clip-path: polygon(9% 0, 100% 0, 100% 100%, 0 100%);
    color: #fff; font-size: 17px; letter-spacing: 2px;
    display: flex; align-items: center; justify-content: flex-end; padding-right: 30px;
  }

  .appointment__title { position: absolute; left: 33px; top: 109px; font-size: 18px; font-weight: 700; color: var(--purple); }
  .slots { position: absolute; left: 33px; top: 178px; width: 582px; display: grid; grid-template-columns: 282px 282px; column-gap: 18px; row-gap: 14px; }
  .slot { height: 25.5px; border-bottom: 1.5px solid var(--grey-line); font-size: 16px; color: var(--purple); line-height: 22px; }
  .notice { position: absolute; left: 33px; top: 346px; font-size: 16px; color: var(--purple); }
</style>
</head>
<body>

<section class="card card--front">
  <div class="brand"><span class="brand__name">Lumen Orto</span><span class="brand__dot"></span></div>

  <div class="holder__accent"></div>
  <div class="holder__name">Carys Whitfield</div>
  <div class="holder__role">Managing Director</div>
  <div class="divider"></div>

  <ul class="contacts">
    <li><svg viewBox="0 0 16 16"><path d="M1 6c0-2 3-3 7-3s7 1 7 3v1h-4V5.5H5V7H1z"/><path d="M4 8h8l2 6H2z"/></svg>+ 000 000 0000</li>
    <li><svg viewBox="0 0 16 16"><rect x="4" y="1" width="8" height="4"/><rect x="1" y="6" width="14" height="6" rx="1"/><rect x="4" y="10" width="8" height="5"/></svg>+ 000 000 0000</li>
    <li><svg viewBox="0 0 16 16"><path d="M1 3h14v1.5L8 9 1 4.5z"/><path d="M1 6l7 4.5L15 6v7H1z"/></svg>info@LumenOrto.co.uk</li>
    <li><svg viewBox="0 0 16 16"><circle cx="8" cy="8" r="6.5" fill="none" stroke="currentColor" style="stroke:var(--purple)" stroke-width="1.6"/><path d="M1.5 8h13M8 1.5c-3 3-3 10 0 13M8 1.5c3 3 3 10 0 13" fill="none" style="stroke:var(--purple)" stroke-width="1.2"/></svg>LumenOrtoReflexology.co.uk</li>
  </ul>

  <address class="address">2748 Marlowe Crest Lane,<br>Harbor Point FL 32190</address>

  <div class="band-grey"></div>
  <div class="band-tagline">Relax, Renew, Revive</div>
</section>

<section class="card card--back">
  <div class="brand"><span class="brand__name">Lumen Orto</span><span class="brand__dot"></span></div>

  <h2 class="appointment__title">APPOINTMENT</h2>
  <div class="slots">
    <div class="slot">Date:</div><div class="slot">Time:</div>
    <div class="slot">Date:</div><div class="slot">Time:</div>
    <div class="slot">Date:</div><div class="slot">Time:</div>
    <div class="slot">Date:</div><div class="slot">Time:</div>
  </div>
  <p class="notice">If you are unable to keep your appointment , please allow 24 hours notice</p>
</section>

</body>
</html>
```